Admin Backend Redesign

We need a redesign for our backend which supoosed to make the backoffice look more modern!

I will add screenshots of the backoffice so you know what data will be shown in the Admin.

Have in mind that the users of this backend are Doctors. We need a clinical look, modern and sharp. The backoffice is responsive, have that in mind. We need the backoffice to look as professional as possible.

The theme used for the website is: http://velmora.brisk-sample.net/

ON the main page of the backoffice, under every widget i need some space to write an explanation what the widget is about.

The color code used in our logo and website is #57aad4 combined with white.

We are open for ideas!
Updates

Project Deadline Extended
Reason: Designs are ok, but nothing innovative. Please use more modern designs!

Project Deadline Extended
Reason: Havent recieved a perfect design yet. Please read instructions carefully! Thank you

Project Deadline Extended
Reason: Hey everybody, sorry for the delay. We will decide in 3 days. If anyone wants to add a Design, that would be great.

Target Market(s)

Doctors, therapists

Industry/Entity Type

It Professional

Font styles to use
Sans Serif

Requirements
Must have
• Must look uptodate, modern, like new back offices look nowadays

```html
<!DOCTYPE html>
<html lang="de">
<head>
<meta charset="utf-8">
<title>Praxis Backoffice – Dashboard</title>
<link href="https://fonts.googleapis.com/css2?family=Open+Sans:wght@300;400;600&display=swap" rel="stylesheet">
<style>
:root{
  --bg:#cfe0e8;
  --topbar:#b3ceda;
  --card:#57aad4;
  --card-head:#4298c8;
  --nav-active:#56a9d4;
  --nav:#4499c8;
  --line:#4a9ccb;
  --white:#ffffff;
  --accent:#22c4b9;
  --accent-edge:#1aa89a;
  --yellow:#ffd97c;
  --teal:#8ef3ef;
  --red:#f88682;
  --grey:#dcdcdc;
  --purple:#c985ec;
  --search-text:#3d8fbf;
}
*{box-sizing:border-box;margin:0;padding:0}
html,body{width:960px;height:1200px;overflow:hidden}
body{background:var(--bg);font-family:"Open Sans",Arial,sans-serif;color:var(--white);position:relative}
.topbar{position:absolute;left:0;top:0;width:960px;height:42px;background:var(--topbar);border-bottom:1px solid #c2d8e2}
.user-menu{position:absolute;left:786px;top:6px;display:flex;align-items:center;gap:8px;font-size:11.5px}
.avatar{width:27px;height:27px;background:linear-gradient(#e8eef2,#c8d3da);border:1px solid #fff}
.caret{font-size:9px;margin-left:4px}
.sidenav{position:absolute;left:88px;top:54px;width:172px}
.sidenav a{display:flex;align-items:center;height:36px;padding-left:10px;gap:9px;font-size:11.5px;color:var(--white);text-decoration:none;background:var(--nav);border-bottom:1px solid #5aaad4}
.sidenav a.active{background:var(--nav-active)}
.sidenav svg{width:20px;height:20px;fill:var(--white)}
.card{position:absolute;width:282px;background:var(--card)}
.card-head{height:31px;background:var(--card-head);font-size:11.5px;display:flex;align-items:center;padding-left:14px}
.col-l{left:275px}.col-r{left:574px}
.hero{height:109px}
.hero-icon{position:absolute;left:20px;top:16px;width:44px;height:46px}
.hero-title{position:absolute;left:81px;top:14px;font-size:25.6px;font-weight:300;line-height:1.1}
.hero-sub{position:absolute;left:81px;top:45px;font-size:14px;font-weight:300;opacity:.92}
.hero-foot{position:absolute;left:0;top:75px;width:100%;height:34px;border-top:1px solid var(--line);display:flex;align-items:center;justify-content:space-between;padding:0 11px;font-size:13px;font-weight:300}
.hero-foot svg{width:15px;height:13px}
.welcome-head svg{width:20px;height:15px;margin-right:9px}
.welcome-body{padding:12px 11px 0 12px;font-size:11.2px;line-height:13.4px}
.welcome-body p{margin-bottom:10px}
.btn-ok{display:block;width:107px;height:31px;margin-left:-3px;background:var(--accent);border:1px solid var(--accent-edge);color:var(--white);font-size:11.5px;line-height:29px;text-align:center}
.chart{position:absolute;left:0;top:31px}
.legend{position:absolute;left:200px;top:58px;font-size:11.5px;list-style:none}
.legend li{display:flex;align-items:center;height:17.6px}
.legend i{display:inline-block;width:9px;height:9px;margin-right:6px}
.search{position:absolute;left:9px;top:41px;width:266px;height:25px;background:var(--white);color:var(--search-text);font-size:9.5px;display:flex;align-items:center;justify-content:space-between;padding:0 9px}
.search svg{width:14px;height:14px}
.th,.td{position:absolute;white-space:nowrap}
.th{font-size:11.2px;top:78px}
.th .sort{font-size:6px;margin-right:2px;vertical-align:1px}
.rule{position:absolute;left:9px;top:98px;width:261px;height:1px;background:var(--white);opacity:.8}
.td{font-size:9.6px}
.bar{position:absolute;height:10px;background:var(--white)}
.tri{font-size:6px;margin-right:3px;vertical-align:1px}
.stars{letter-spacing:-1px;font-size:8px}
.foot{position:absolute;left:0;top:214px;width:100%;height:31px;border-top:1px solid var(--line)}
.foot-text{position:absolute;left:12px;top:6px;font-size:11.2px}
.pager{position:absolute;left:212px;top:7px;display:flex;gap:1px}
.pager span{width:14px;height:16px;background:var(--white);color:var(--search-text);font-size:9.5px;display:flex;align-items:center;justify-content:center}
.pager span.wide{width:16px}
</style>
</head>
<body>
<header class="topbar">
  <div class="user-menu"><div class="avatar" role="img" aria-label="Profilfoto des Arztes"></div><span>Dr.</span><span class="caret">▼</span></div>
</header>

<nav class="sidenav">
  <a class="active" href="#"><svg viewBox="0 0 20 20"><path d="M10 2 1 10h3v8h4.5v-5h3v5H16v-8h3z"/></svg>Dashboard</a>
  <a href="#"><svg viewBox="0 0 20 20"><circle cx="10" cy="5.5" r="4"/><path d="M2 20c0-6 3-9 8-9s8 3 8 9z"/></svg>Mien Konto</a>
  <a href="#"><svg viewBox="0 0 20 20"><circle cx="10" cy="5.5" r="4"/><path d="M2 20c0-6 3-9 8-9s8 3 8 9z"/></svg>Patientenbewertungen</a>
</nav>

<section class="card hero col-l" style="top:54px">
  <svg class="hero-icon" viewBox="0 0 44 46" fill="#fff"><circle cx="22" cy="11" r="9"/><path d="M4 46c0-15 7-22 18-22s18 7 18 22z"/><path d="M14 26v8a6 6 0 0 0 12 0" fill="none" stroke="#57aad4" stroke-width="2"/><circle cx="30" cy="38" r="3" fill="#57aad4"/><path d="M8 38h6M11 35v6" stroke="#57aad4" stroke-width="2"/></svg>
  <div class="hero-title">Profil</div>
  <div class="hero-sub">Profile bearbeiten</div>
  <div class="hero-foot"><span>WEITER</span><svg viewBox="0 0 15 13" fill="none" stroke="#fff" stroke-width="2"><path d="M0 6.5h13M8 1l5.5 5.5L8 12"/></svg></div>
</section>

<section class="card hero col-r" style="top:54px">
  <svg class="hero-icon" viewBox="0 0 44 46" fill="#fff"><circle cx="22" cy="11" r="9"/><path d="M4 46c0-15 7-22 18-22s18 7 18 22z"/><rect x="20" y="33" width="18" height="9" rx="4.5" fill="#57aad4"/><rect x="22" y="35" width="14" height="5" rx="2.5"/></svg>
  <div class="hero-title">Patienten</div>
  <div class="hero-sub">Patienten verwalten</div>
  <div class="hero-foot"><span>ALLE ANSEHEN</span><svg viewBox="0 0 15 13" fill="none" stroke="#fff" stroke-width="2"><path d="M0 6.5h13M8 1l5.5 5.5L8 12"/></svg></div>
</section>

<section class="card col-l" style="top:179px;height:167px">
  <div class="card-head welcome-head" style="padding-left:11px"><svg viewBox="0 0 20 15"><rect x="1" y="1" width="18" height="13" fill="none" stroke="#fff" stroke-width="1.5"/><path d="M2 13l5-6 4 4 3-3 5 5z" fill="#fff"/><circle cx="14" cy="5" r="1.6" fill="#fff"/></svg>Willkommen: Dr. Mustermann</div>
  <div class="welcome-body">
    <p>Der Status Ihres offentlichen Profils ist derzeit:</p>
    <p>Lorem ipsum dolor sit amet, consectetur adipisicing elit, sed do eiusmod tempor incididunt ut labore et dolore magna aliqua. Ut enim ad minim veniam,</p>
    <span class="btn-ok">Alles OK</span>
  </div>
</section>

<section class="card col-r" style="top:179px;height:167px">
  <div class="card-head" style="padding-left:18px">kelvo Trend fur:</div>
  <svg style="position:absolute;left:0;top:0" width="282" height="167" viewBox="0 0 282 167">
    <g fill="#fff" font-size="8.5" font-family="Open Sans, sans-serif">
      <text x="20" y="50" text-anchor="end">15</text>
      <text x="20" y="84" text-anchor="end">10</text>
      <text x="20" y="114" text-anchor="end">5</text>
      <text x="20" y="146" text-anchor="end">0</text>
      <text x="50" y="159" text-anchor="middle">Oct 2012</text>
      <text x="99" y="159" text-anchor="middle">Jan 2013</text>
      <text x="149" y="159" text-anchor="middle">Apr 2013</text>
      <text x="197" y="159" text-anchor="middle">Jul 2013</text>
      <text x="246" y="159" text-anchor="middle">Oct 2013</text>
    </g>
    <path d="M24 43V143H262" fill="none" stroke="#fff" stroke-width="1"/>
    <polyline fill="none" stroke="#fff" stroke-width="1.2" points="24,143.4 98.8,143.4 106,91.4 115.6,81 121.2,89.8 127.6,87.4 133.2,41.8 138,53 152.4,103.4 167.6,113 175.6,98.6 188.4,117.8 198.8,91.4 207.6,99.4 222,86.6 233.2,92.2 238,85.8 244.4,93.8 250.8,85 262,85.8"/>
  </svg>
</section>

<section class="card col-l" style="top:362px;height:226px">
  <div class="card-head">Pie 1</div>
  <svg class="chart" width="282" height="195" viewBox="0 0 282 195">
    <path d="M94 93L94 19A74 74 0 0 1 111.9 164.8Z" fill="var(--yellow)"/>
    <path d="M94 93L111.9 164.8A74 74 0 0 1 49.5 152.1Z" fill="var(--teal)"/>
    <path d="M94 93L49.5 152.1A74 74 0 0 1 94 19Z" fill="var(--red)"/>
  </svg>
  <ul class="legend">
    <li><i style="background:var(--yellow)"></i>Series 1</li>
    <li><i style="background:var(--teal)"></i>Series 2</li>
    <li><i style="background:var(--red)"></i>Series 3</li>
  </ul>
</section>

<section class="card col-r" style="top:362px;height:226px">
  <div class="card-head">Pie 2</div>
  <svg class="chart" width="282" height="195" viewBox="0 0 282 195">
    <path d="M94 93L94 19A74 74 0 0 1 111.9 21.2Z" fill="var(--yellow)"/>
    <path d="M94 93L111.9 21.2A74 74 0 0 1 158.5 56.7Z" fill="var(--teal)"/>
    <path d="M94 93L158.5 56.7A74 74 0 0 1 111.9 164.8Z" fill="var(--red)"/>
    <path d="M94 93L111.9 164.8A74 74 0 0 1 49.5 152.1Z" fill="var(--grey)"/>
    <path d="M94 93L49.5 152.1A74 74 0 0 1 94 19Z" fill="var(--purple)"/>
  </svg>
  <ul class="legend">
    <li><i style="background:var(--yellow)"></i>Series 1</li>
    <li><i style="background:var(--teal)"></i>Series 2</li>
    <li><i style="background:var(--red)"></i>Series 3</li>
    <li><i style="background:var(--grey)"></i>Series 5</li>
    <li><i style="background:var(--purple)"></i>Series 6</li>
  </ul>
</section>

<section class="card col-l" style="top:604px;height:246px">
  <div class="card-head">Stat 1</div>
  <div class="search"><span>search</span><svg viewBox="0 0 14 14" fill="none" stroke="#3d8fbf" stroke-width="2"><circle cx="5.5" cy="5.5" r="4.3"/><path d="M8.7 8.7L13 13"/></svg></div>
  <span class="th" style="left:13px">Name</span>
  <span class="th" style="left:69px"><span class="sort">▲▼</span>Position</span>
  <span class="th" style="left:134px"><span class="sort">▲▼</span>Start Date</span>
  <span class="th" style="left:216px"><span class="sort">▲▼</span>Salary</span>
  <div class="rule"></div>
  <span class="td" style="left:13px;top:112px">Gerdan</span><span class="td" style="left:76px;top:112px">Chefin</span><span class="td" style="left:145px;top:112px">1.11.2013</span><span class="td" style="left:223px;top:112px">Salami</span>
  <span class="td" style="left:13px;top:130px">Gerdan</span><span class="td" style="left:76px;top:130px">Chefin</span><span class="td" style="left:145px;top:130px">1.11.2013</span><span class="td" style="left:223px;top:130px">Salami</span>
  <span class="td" style="left:13px;top:149px">Gerdan</span><span class="td" style="left:76px;top:149px">Chefin</span><span class="td" style="left:145px;top:149px">1.11.2013</span><span class="td" style="left:223px;top:149px">Salami</span>
  <span class="td" style="left:13px;top:167px">Gerdan</span><span class="td" style="left:76px;top:167px">Chefin</span><span class="td" style="left:145px;top:167px">1.11.2013</span><span class="td" style="left:223px;top:167px">Salami</span>
  <span class="td" style="left:13px;top:185px">Gerdan</span><span class="td" style="left:76px;top:185px">Chefin</span><span class="td" style="left:145px;top:185px">1.11.2013</span><span class="td" style="left:223px;top:185px">Salami</span>
  <div class="foot"><span class="foot-text">Showing 1 to 5 of 9 entries</span><div class="pager"><span class="wide">←</span><span>1</span><span>2</span><span class="wide">→</span></div></div>
</section>

<section class="card col-r" style="top:604px;height:246px">
  <div class="card-head">Stat 2</div>
  <div class="search"><span>search</span><svg viewBox="0 0 14 14" fill="none" stroke="#3d8fbf" stroke-width="2"><circle cx="5.5" cy="5.5" r="4.3"/><path d="M8.7 8.7L13 13"/></svg></div>
  <span class="th" style="left:12px">Domain</span>
  <span class="th" style="left:70px"><span class="sort">▲▼</span>Niveau</span>
  <span class="th" style="left:135px"><span class="sort">▲▼</span>Keyw.</span>
  <span class="th" style="left:216px"><span class="sort">▲▼</span>Seyw.</span>
  <div class="rule"></div>
  <span class="td" style="left:12px;top:112px">domain1.de</span><span class="bar" style="left:77px;top:113px;width:7px"></span><span class="td" style="left:136px;top:112px">Gemeinsame K</span><span class="td" style="left:220px;top:112px">SE Keyw</span>
  <span class="td" style="left:12px;top:131px">domain1.de</span><span class="bar" style="left:77px;top:132px;width:14px"></span><span class="td" style="left:136px;top:131px">Gemeinsame K</span><span class="td" style="left:220px;top:131px">SE Keyw</span>
  <span class="td" style="left:12px;top:149px">domain1.de</span><span class="bar" style="left:77px;top:150px;width:22px"></span><span class="td" style="left:136px;top:149px">Gemeinsame K</span><span class="td" style="left:220px;top:149px">SE Keyw</span>
  <span class="td" style="left:12px;top:167px">domain1.de</span><span class="bar" style="left:77px;top:168px;width:34px"></span><span class="td" style="left:136px;top:167px">Gemeinsame K</span><span class="td" style="left:220px;top:167px">SE Keyw</span>
  <span class="td" style="left:12px;top:186px">domain1.de</span><span class="bar" style="left:77px;top:187px;width:48px"></span><span class="td" style="left:136px;top:186px">Gemeinsame K</span><span class="td" style="left:220px;top:186px">SE Keyw</span>
  <div class="foot"><span class="foot-text">Showing 1 to 5 of 9 entries</span><div class="pager"><span class="wide">←</span><span>1</span><span>2</span><span class="wide">→</span></div></div>
</section>

<section class="card col-l" style="top:866px;height:245px">
  <div class="card-head">Sternchen</div>
  <div class="search"><span>search</span><svg viewBox="0 0 14 14" fill="none" stroke="#3d8fbf" stroke-width="2"><circle cx="5.5" cy="5.5" r="4.3"/><path d="M8.7 8.7L13 13"/></svg></div>
  <span class="th" style="left:13px">Name</span>
  <span class="th" style="left:122px"><span class="sort">▲▼</span>Profilsiete</span>
  <span class="th" style="left:199px"><span class="sort">▲▼</span>Bewertung</span>
  <div class="rule"></div>
  <span class="td" style="left:13px;top:111px"><span class="tri">▶</span>ciao!</span><span class="td" style="left:136px;top:111px"><span class="tri">▶</span>xyz ungelost</span><span class="td stars" style="left:226px;top:112px">★★★★★</span>
  <span class="td" style="left:13px;top:129px"><span class="tri">▶</span>praxilo.de</span><span class="td" style="left:136px;top:129px"><span class="tri">▶</span>xyz ungelost</span><span class="td stars" style="left:226px;top:130px">★★★★★</span>
  <span class="td" style="left:13px;top:148px"><span class="tri">▶</span>DIE ARZTAUSWAHL</span><span class="td" style="left:136px;top:148px"><span class="tri">▶</span>xyz ungelost</span><span class="td stars" style="left:226px;top:149px">★★★★★</span>
  <span class="td" style="left:13px;top:166px"><span class="tri">▶</span>DIE ENDVERBRAUCHER</span><span class="td" style="left:136px;top:166px"><span class="tri">▶</span>xyz ungelost</span><span class="td stars" style="left:226px;top:167px">★★★★★</span>
  <span class="td" style="left:13px;top:185px"><span class="tri">▶</span>DIE ENDVERBRAUCHER</span><span class="td" style="left:136px;top:185px"><span class="tri">▶</span>xyz ungelost</span><span class="td stars" style="left:226px;top:186px">★★★★★</span>
  <div class="foot"><span class="foot-text">Showing 1 to 5 of 9 entries</span><div class="pager"><span class="wide">←</span><span>1</span><span>2</span><span class="wide">→</span></div></div>
</section>
</body>
</html>
```